Simple and clean webdesign for personal homepage

Trying to create a simple and clean webdesign for my personal homepage. Going to use a static site builder with templates to build the site. I want it to have multiple pages - like an about me, blog and resume. I just need something very basic I can customize. I want the main colors to be purple, black and white. I am open to other color palettes too but since purple is my favorite color I want that to be one of the main colors.

The site be mostly text driven. Might have some images in the body text but I want the site design to be light and lean.

Industry/Entity Type

Personal Homepage.

Coding

Coded - Design and coding required

Number of Pages Required

1 page

Font styles to use
Sans Serif

Colors
6B429C
8869AF
B7A5CE
E3DAEB
F3F0F8

Requirements
Must have
• Clean design. Purple used as a color. HTML template.
Nice to have
• Responsive

```html
<!DOCTYPE html>
<html lang="en">
<head>
<meta charset="utf-8">
<title>Personal Homepage</title>
<link href="https://fonts.googleapis.com/css2?family=Playfair+Display:wght@400;700&family=Poppins:wght@400;500&display=swap" rel="stylesheet">
<style>
:root{
  --purple-deep:#6B429C;
  --purple-mid:#8869AF;
  --purple-soft:#B7A5CE;
  --purple-pale:#E3DAEB;
  --purple-mist:#F3F0F8;
  --ink:#111111;
  --text:#2a2a2a;
  --white:#ffffff;
}
*{box-sizing:border-box;margin:0;padding:0}
html,body{width:1200px;height:4376px;overflow:hidden}
body{font-family:'Poppins',sans-serif;color:var(--text);background:var(--white)}
.serif{font-family:'Playfair Display',serif}
h1,h2,h3{font-family:'Playfair Display',serif}

/* Hero */
.hero{position:relative;height:641px;color:var(--white);
  background:radial-gradient(ellipse at 30% 70%,#9a7cc7 0%,rgba(154,124,199,0) 55%),
             linear-gradient(180deg,#8c68c2 0%,#7a55b5 45%,#8a67c0 100%);}
.nav{position:absolute;top:30px;left:170px;right:172px;display:flex;justify-content:space-between;align-items:center}
.logo{font-family:'Playfair Display',serif;font-size:42px;font-weight:400;letter-spacing:.5px}
.nav-links{display:flex;gap:28px;font-family:'Playfair Display',serif;font-size:22px}
.hero-content{position:absolute;top:190px;left:0;right:0;text-align:center}
.hero-title{font-size:54px;font-weight:700}
.hero-text{margin:26px auto 0;width:600px;font-size:18px;line-height:27px}
.btn-outline{display:inline-flex;align-items:center;justify-content:center;margin-top:30px;width:226px;height:70px;border:2px solid var(--white);border-radius:0 36px 36px 36px;font-family:'Playfair Display',serif;font-weight:700;font-size:20px}

/* Section titles */
.section-title{font-size:50px;font-weight:700;color:var(--purple-deep);text-transform:uppercase;text-align:center}

/* About */
.about{height:605px;padding-top:738px - 641px;text-align:center}
.about{padding-top:97px}
.about-text{width:806px;margin:20px auto 0;font-size:18px;line-height:29px;color:var(--text)}
.btn-solid{display:inline-flex;align-items:center;justify-content:center;width:296px;height:80px;background:var(--purple-deep);color:var(--white);border-radius:0 40px 40px 0;font-family:'Playfair Display',serif;font-weight:700;font-size:18px}
.about .btn-solid{margin-top:44px}

/* Mail list */
.mail{height:376px;text-align:center;color:var(--white);padding-top:57px;
  background:linear-gradient(180deg,#b7a5ce 0%,#c2b3d6 50%,#b3a0cb 100%)}
.mail .section-title{color:var(--white)}
.mail-text{width:660px;margin:14px auto 0;font-size:18px;line-height:29px}
.mail-form{display:flex;justify-content:center;margin-top:30px}
.mail-input{width:450px;height:55px;background:var(--white);border-radius:28px 0 0 28px;display:flex;align-items:center;padding-left:38px;font-family:'Playfair Display',serif;font-size:11px;color:var(--purple-deep);letter-spacing:.3px}
.mail-button{width:180px;height:55px;background:var(--purple-deep);border-radius:0 28px 28px 0;display:flex;align-items:center;justify-content:center;font-family:'Playfair Display',serif;font-size:18px}

/* Courses */
.courses{height:821px;padding-top:97px;text-align:center}
.course-grid{display:grid;grid-template-columns:462px 462px;column-gap:0;margin:52px 0 0 171px;row-gap:46px;text-align:left}
.course{display:flex;gap:14px}
.course-icon{flex:none;width:106px;height:106px;border-radius:50%;background:var(--purple-deep);box-shadow:0 0 0 6px var(--purple-mist);display:flex;align-items:center;justify-content:center;margin-top:12px}
.course-title{font-size:22px;font-weight:700;line-height:27px;color:var(--ink)}
.course-text{margin-top:14px;font-size:17px;line-height:22px;width:285px}
.courses .btn-solid{margin-top:56px}

/* Blog */
.blog{height:1565px;padding-top:60px;text-align:center;
  background:linear-gradient(180deg,var(--purple-pale) 0%,#e0d6ea 60%,#dcd2e6 100%)}
.blog-grid{display:grid;grid-template-columns:repeat(3,275px);gap:20px 16px;justify-content:center;margin-top:40px;margin-left:-1px}
.card{height:393px;background:var(--white);padding:15px 13px 0;box-shadow:0 2px 10px rgba(107,66,156,.12);position:relative}
.card-img{height:170px}
.date{width:150px;height:44px;margin:-22px auto 0;position:relative;background:var(--purple-deep);color:var(--white);border-radius:22px;font-size:17px;display:flex;align-items:center;justify-content:center}
.card-title{margin-top:16px;font-size:18px;font-weight:700;line-height:27px;color:var(--ink)}
.card-text{margin-top:10px;font-size:13px;line-height:19px;color:#333}
.pager{display:flex;justify-content:center;gap:10px;margin-top:54px}
.page{width:44px;height:44px;border-radius:50%;background:var(--white);color:#999;font-family:'Playfair Display',serif;font-size:18px;display:flex;align-items:center;justify-content:center}
.page.active{background:var(--purple-deep);color:var(--white)}

/* Footer */
.footer{height:368px;text-align:center;color:var(--white);padding-top:140px;
  background:radial-gradient(ellipse at 50% 40%,#9578b9 0%,rgba(149,120,185,0) 60%),var(--purple-mid)}
.footer-links{display:flex;justify-content:center;gap:28px;font-family:'Playfair Display',serif;font-size:28px}
.social{display:flex;justify-content:center;gap:20px;margin-top:32px}
.social span{width:54px;height:54px;border-radius:50%;background:var(--white)}
.copyright{margin-top:28px;font-family:'Playfair Display',serif;font-size:14px}
</style>
</head>
<body>

<header class="hero" role="img" aria-label="Field of lavender in soft purple light">
  <nav class="nav">
    <div class="logo">LOGO NAME</div>
    <div class="nav-links"><span>Home</span><span>About me</span><span>Blog</span><span>Resume</span></div>
  </nav>
  <div class="hero-content">
    <h1 class="hero-title">Lorem ipsum dolor sit amet</h1>
    <p class="hero-text">Lorem ipsum dolor sit amet, consectetur adipiscing elit, sed do eiusmod tempor incididunt ut labore et dolore magna aliqua.</p>
    <span class="btn-outline">READ MORE</span>
  </div>
</header>

<section class="about">
  <h2 class="section-title">About me</h2>
  <p class="about-text">Lorem ipsum dolor sit amet, consectetur adipiscing elit, sed do eiusmod tempor incid idunt ut labore et dolore magna aliqua. Ut enim ad minim veniam, quis nostruloremd exercitation ullamco laboris nisi ut aliquip ex ea commodo consequat.Duis aute irure do reprehenderit in voluptate velit esse cillum dolore eu fugiat nulla pariatur.m ipsum dolor sit amet, consectetur adipiscing elit, sed do eiusmod tempor inciidunt ut labore et dolore magna aliqua. Ut enim ad minim veniam, quis nostruloremd exercitation atur.</p>
  <span class="btn-solid">DOWNLOAD MY RESUME</span>
</section>

<section class="mail" role="img" aria-label="Faded photo of a person with open arms in a lavender meadow">
  <h2 class="section-title">Mail list registration</h2>
  <p class="mail-text">Lorem ipsum dolor sit amet, consectetur adipiscing elit, sed do eiusmod tempor incididunt ut labore et dolore magna aliqua.</p>
  <div class="mail-form">
    <div class="mail-input">ENTER YOUR EMAIL</div>
    <div class="mail-button">REGISTER NOW</div>
  </div>
</section>

<section class="courses">
  <h2 class="section-title">Courses</h2>
  <div class="course-grid">
    <div class="course">
      <div class="course-icon">
        <svg width="54" height="54" viewBox="0 0 54 54" fill="none" stroke="#fff" stroke-width="2" stroke-linecap="round">
          <path d="M20 33c-3-3-5-6-5-10a12 12 0 0 1 24 0c0 4-2 7-5 10v4H20z"/>
          <path d="M21 41h12M22 45h10"/>
          <path d="M24 33v-8l3 3 3-3v8"/>
          <path d="M27 4v4M9 23H5M49 23h-4M13 10l3 3M41 10l-3 3"/>
        </svg>
      </div>
      <div>
        <h3 class="course-title">Lorem ipsum dolormsed ldummynsit amet</h3>
        <p class="course-text">Lorem ipsum dolor sit ametcon sectetur adipiscing elit, sed lodo eiusmod tempor incididunt ut labore et dolore magna ua.</p>
      </div>
    </div>
    <div class="course">
      <div class="course-icon">
        <svg width="54" height="54" viewBox="0 0 54 54" fill="none" stroke="#fff" stroke-width="2" stroke-linecap="round" stroke-linejoin="round">
          <path d="M44 10c-10 0-18 5-24 15l9 9c10-6 15-14 15-24z"/>
          <circle cx="34" cy="20" r="3"/>
          <path d="M20 25l-8 1-4 6 9 1M29 34l-1 8-6 4-1-9"/>
          <path d="M16 38l-6 6M13 34l-4 4M20 41l-4 4"/>
        </svg>
      </div>
      <div>
        <h3 class="course-title">Lorem ipsum dolormsed ldummynsit amet</h3>
        <p class="course-text">Lorem ipsum dolor sit ametcon sectetur adipiscing elit, sed lodo eiusmod tempor incididunt ut labore et dolore magna ua.</p>
      </div>
    </div>
    <div class="course">
      <div class="course-icon">
        <svg width="54" height="54" viewBox="0 0 54 54" fill="none" stroke="#fff" stroke-width="2" stroke-linejoin="round">
          <path d="M14 8h18l8 8v28H14z"/>
          <path d="M32 8v8h8"/>
          <path d="M19 50h25V20" />
          <path d="M19 22h16M19 27h16M19 32h16M19 37h12"/>
        </svg>
      </div>
      <div>
        <h3 class="course-title">Lorem ipsum dolormsed ldummynsit amet</h3>
        <p class="course-text">Lorem ipsum dolor sit ametcon sectetur adipiscing elit, sed lodo eiusmod tempor incididunt ut labore et dolore magna ua.</p>
      </div>
    </div>
    <div class="course">
      <div class="course-icon">
        <svg width="54" height="54" viewBox="0 0 54 54" fill="none" stroke="#fff" stroke-width="2" stroke-linecap="round">
          <circle cx="25" cy="29" r="18"/>
          <circle cx="25" cy="29" r="12"/>
          <circle cx="25" cy="29" r="6"/>
          <path d="M25 29l20-20M40 9h5v5M38 11l-1 6 6-1"/>
        </svg>
      </div>
      <div>
        <h3 class="course-title">Lorem ipsum dolormsed ldummynsit amet</h3>
        <p class="course-text">Lorem ipsum dolor sit ametcon sectetur adipiscing elit, sed lodo eiusmod tempor incididunt ut labore et dolore magna ua.</p>
      </div>
    </div>
  </div>
  <span class="btn-solid">DOWNLOAD MY RESUME</span>
</section>

<section class="blog">
  <h2 class="section-title">Blog</h2>
  <div class="blog-grid">
    <article class="card">
      <div class="card-img" role="img" aria-label="Butterfly over lavender flowers" style="background:linear-gradient(160deg,#c9d6ee 0%,#9aa6d8 55%,#6e5fb0 100%)"></div>
      <div class="date">21-12-2021</div>
      <h3 class="card-title">Lorem Ipsum is dummy typesetting industry.</h3>
      <p class="card-text">Lorem ipsum is simply dummy text of the printing and typesetting ever since the 1500s.</p>
    </article>
    <article class="card">
      <div class="card-img" role="img" aria-label="Hands typing on a laptop outdoors" style="background:linear-gradient(150deg,#8a9a6e 0%,#c9b9a2 45%,#6f6c72 100%)"></div>
      <div class="date">21-12-2021</div>
      <h3 class="card-title">Lorem Ipsum is dummy typesetting industry.</h3>
      <p class="card-text">Lorem ipsum is simply dummy text of the printing and typesetting ever since the 1500s.</p>
    </article>
    <article class="card">
      <div class="card-img" role="img" aria-label="Woman holding a cup in a cafe" style="background:linear-gradient(150deg,#5a4640 0%,#b08a78 50%,#e6d4c6 100%)"></div>
      <div class="date">21-12-2021</div>
      <h3 class="card-title">Lorem Ipsum is dummy typesetting industry.</h3>
      <p class="card-text">Lorem ipsum is simply dummy text of the printing and typesetting ever since the 1500s.</p>
    </article>
    <article class="card">
      <div class="card-img" role="img" aria-label="Hands on a laptop keyboard" style="background:linear-gradient(140deg,#3f3a36 0%,#a07a5e 45%,#d8c2ac 100%)"></div>
      <div class="date">21-12-2021</div>
      <h3 class="card-title">Lorem Ipsum is dummy typesetting industry.</h3>
      <p class="card-text">Lorem ipsum is simply dummy text of the printing and typesetting ever since the 1500s.</p>
    </article>
    <article class="card">
      <div class="card-img" role="img" aria-label="Boat on a beach at sunset" style="background:linear-gradient(180deg,#e8c9c0 0%,#d7a9a2 50%,#b98884 100%)"></div>
      <div class="date">21-12-2021</div>
      <h3 class="card-title">Lorem Ipsum is dummy typesetting industry.</h3>
      <p class="card-text">Lorem ipsum is simply dummy text of the printing and typesetting ever since the 1500s.</p>
    </article>
    <article class="card">
      <div class="card-img" role="img" aria-label="Woman among purple leaves" style="background:linear-gradient(150deg,#b58cc4 0%,#8a4e94 50%,#d2b6dc 100%)"></div>
      <div class="date">21-12-2021</div>
      <h3 class="card-title">Lorem Ipsum is dummy typesetting industry.</h3>
      <p class="card-text">Lorem ipsum is simply dummy text of the printing and typesetting ever since the 1500s.</p>
    </article>
    <article class="card">
      <div class="card-img" role="img" aria-label="Purple sunset over the sea" style="background:linear-gradient(180deg,#7a5fc0 0%,#c27ab8 45%,#5a3f9c 100%)"></div>
      <div class="date">21-12-2021</div>
      <h3 class="card-title">Lorem Ipsum is dummy typesetting industry.</h3>
      <p class="card-text">Lorem ipsum is simply dummy text of the printing and typesetting ever since the 1500s.</p>
    </article>
    <article class="card">
      <div class="card-img" role="img" aria-label="Sun setting over a lavender field" style="background:linear-gradient(180deg,#e3a468 0%,#a86a8e 45%,#5c3d80 100%)"></div>
      <div class="date">21-12-2021</div>
      <h3 class="card-title">Lorem Ipsum is dummy typesetting industry.</h3>
      <p class="card-text">Lorem ipsum is simply dummy text of the printing and typesetting ever since the 1500s.</p>
    </article>
    <article class="card">
      <div class="card-img" role="img" aria-label="Purple water lily among green leaves" style="background:radial-gradient(circle at 50% 45%,#b06de0 0%,#7a3fb8 25%,#1f3a26 60%,#0f1f14 100%)"></div>
      <div class="date">21-12-2021</div>
      <h3 class="card-title">Lorem Ipsum is dummy typesetting industry.</h3>
      <p class="card-text">Lorem ipsum is simply dummy text of the printing and typesetting ever since the 1500s.</p>
    </article>
  </div>
  <div class="pager">
    <span class="page active">01</span>
    <span class="page">02</span>
    <span class="page">03</span>
    <span class="page">04</span>
    <span class="page"><svg width="18" height="18" viewBox="0 0 18 18" fill="none" stroke="#999" stroke-width="2" stroke-linecap="round"><path d="M6 3l6 6-6 6"/></svg></span>
  </div>
</section>

<footer class="footer" role="img" aria-label="Faded photo of a person with raised arms in a meadow">
  <div class="footer-links"><span>Home</span><span>About me</span><span>Courses</span><span>Blog</span><span>Resume</span></div>
  <div class="social" aria-label="Social links">
    <span></span><span></span><span></span><span></span><span></span>
  </div>
  <p class="copyright">Copyright © 2022 Company name. All rights reserved.</p>
</footer>

</body>
</html>
```